Brightmoor Partners Branding Revamp

We are a consulting company, looking for a way to display and promote our brand. We have 2 sides to the business- Brightmoor (financial) and Partners (cyber security). The financial side products relate to business necessities: card processing, website design/hosting/maintenance, VoIP phone systems. The cyber security side promotes a bundled package of 4 solutions: network vulnerability scan, dark web scan, anti-ransomeware/malware software, and image-level backups. We want people to understand that partnering with Brightmoor Partners gives them “Elevated Peace of Mind” (tagline). Current badge and logos uploaded.

Target Market(s)

Small businesses

Contact Information for Business Card

Lena Marwick, Vice President, lena@brightmoorpartners.example, 555-806-1937, www.brightmoorpartners.example

Requirements
Nice to have
• I do prefer the darker background for front and back

```html
<!DOCTYPE html>
<html lang="en">
<head>
<meta charset="utf-8">
<title>Brightmoor Partners — Business Card</title>
<link rel="stylesheet" href="https://fonts.googleapis.com/css2?family=Roboto:wght@400;700&display=swap">
<style>
  :root {
    --page: #ffffff;
    --card-red: #e8262d;
    --card-red-light: #f2464a;
    --card-red-dark: #c9151c;
    --card-dark: #353436;
    --ink-light: #ffffff;
    --ink-muted: #e6e6e6;
  }
  * { box-sizing: border-box; margin: 0; padding: 0; }
  html, body {
    width: 1200px;
    height: 1012px;
    overflow: hidden;
    background: var(--page);
    font-family: "Roboto", Arial, sans-serif;
  }
  .sheet {
    position: relative;
    width: 1200px;
    height: 1012px;
  }
  .card {
    position: absolute;
    top: 347px;
    width: 555px;
    height: 317px;
    overflow: hidden;
  }
  .card--front { left: 20px; }
  .card--back { left: 625px; background: var(--card-dark); }

  /* front */
  .front-pattern {
    position: absolute;
    inset: 0;
    background: radial-gradient(ellipse at 35% 40%, var(--card-red-light) 0%, var(--card-red) 55%, var(--card-red-dark) 100%);
  }
  .front-brand {
    position: absolute;
    right: 40px;
    top: 170px;
    display: flex;
    align-items: center;
    gap: 8px;
    color: var(--ink-light);
    font-weight: 700;
    font-size: 17px;
    white-space: nowrap;
  }
  .front-brand__mark {
    width: 14px;
    height: 14px;
    background: var(--ink-light);
  }
  .front-web {
    position: absolute;
    right: 40px;
    top: 242px;
    color: var(--ink-light);
    font-size: 13px;
    white-space: nowrap;
  }

  /* back */
  .back-brand {
    position: absolute;
    right: 30px;
    top: 118px;
    display: flex;
    align-items: center;
    gap: 10px;
    color: var(--ink-light);
    font-weight: 700;
    font-size: 20px;
    letter-spacing: 2px;
    text-transform: uppercase;
    white-space: nowrap;
  }
  .back-brand__mark {
    width: 16px;
    height: 16px;
    background: var(--card-red);
  }
  .holder__bar {
    position: absolute;
    left: 4px;
    top: 180px;
    width: 14px;
    height: 37px;
    background: var(--ink-light);
  }
  .holder__name {
    position: absolute;
    left: 29px;
    top: 177px;
    color: var(--ink-light);
    font-weight: 700;
    font-size: 20px;
  }
  .holder__title {
    position: absolute;
    left: 29px;
    top: 201px;
    color: var(--ink-muted);
    font-size: 16px;
  }
  .holder__rule {
    position: absolute;
    left: 146px;
    right: 31px;
    top: 214px;
    height: 2px;
    background: var(--ink-light);
  }
  .contacts {
    position: absolute;
    right: 30px;
    top: 226px;
    list-style: none;
    text-align: right;
  }
  .contacts__item {
    display: flex;
    justify-content: flex-end;
    align-items: center;
    gap: 4px;
    height: 23px;
    color: var(--ink-light);
    font-size: 16px;
    white-space: nowrap;
  }
  .contacts__icon { width: 14px; height: 14px; flex: none; }
</style>
</head>
<body>
<main class="sheet">

  <section class="card card--front" aria-label="Card front">
    <div class="front-pattern" role="img" aria-label="Red faceted geometric background pattern"></div>
    <div class="front-brand"><span class="front-brand__mark"></span>Brightmoor Partners</div>
    <p class="front-web">www.brightmoorpartners.example</p>
  </section>

  <section class="card card--back" aria-label="Card back">
    <div class="back-brand"><span class="back-brand__mark"></span>Brightmoor Partners</div>

    <span class="holder__bar"></span>
    <h1 class="holder__name">Lena Marwick</h1>
    <p class="holder__title">Vice President</p>
    <span class="holder__rule"></span>

    <ul class="contacts">
      <li class="contacts__item">lena@brightmoorpartners.example
        <svg class="contacts__icon" viewBox="0 0 14 14" aria-hidden="true">
          <rect x="0.5" y="3" width="13" height="9" fill="#fff"/>
          <path d="M0.5 3 L7 8 L13.5 3" fill="none" stroke="#353436" stroke-width="1.2"/>
        </svg>
      </li>
      <li class="contacts__item">555-806-1937
        <svg class="contacts__icon" viewBox="0 0 14 14" aria-hidden="true">
          <rect x="4" y="1" width="6.5" height="12" rx="1.2" fill="none" stroke="#fff" stroke-width="1.2"/>
          <line x1="6" y1="11" x2="8.5" y2="11" stroke="#fff" stroke-width="1"/>
        </svg>
      </li>
      <li class="contacts__item">www.brightmoorpartners.example
        <svg class="contacts__icon" viewBox="0 0 14 14" aria-hidden="true">
          <g fill="none" stroke="#fff" stroke-width="1">
            <circle cx="7" cy="7" r="6"/>
            <ellipse cx="7" cy="7" rx="2.6" ry="6"/>
            <line x1="1" y1="7" x2="13" y2="7"/>
            <line x1="2" y1="4" x2="12" y2="4"/>
            <line x1="2" y1="10" x2="12" y2="10"/>
          </g>
        </svg>
      </li>
    </ul>
  </section>

</main>
</body>
</html>
```